Premium Relish Company Needs Postcard size Shelf talker

Business name: Bramwell & Jory Velvet Foods
www.bramwellandjory.com.au
Product/service/brand name:
Bramwell & Jory Velvet Foods. We produce the MOST delicious premium relishes in Australia and they retail in all premium deli’s, butchers, and high end supermarkets in NSW and VIC. Please see our website for further details: www.bramwellandjory.com.au
Key Objective:
Design a Post card size shelf talker. These are small signs that attach to a retail shelf ledge. Shelf Talkers are an effective way to attract and communicate with customer's in-store as they are wandering the aisles. OUR key objective is to attract EVERY single potential customer to the relish and make them buy.
Marketing objectives:
Build Brand awareness, Increase sales by creating enough curiosity for a customer to purchase the product immediately without trying it. We want something that will catch the eye and increase their interest until picking up the product off the shelf and putting it in their basket seems the most logical and sensible option to them, as opposed to them feeling they are involved in a great risk.
Our Image:
We like humour and our two phrases "Relish just got saucy" & "Makes everything better. - EVERYTHING!" reflect this. We like to appeal to their happier side when they purchase our product.
We don't want busy imagery.
Please avoid the brash colours and imagery associated with take away food. This is premium cuisine, with a modern urban angle – but not up itself. It is the perfect accompaniment to a fantastic quality BBQ for average Australian and the perfect condiment to always keep in the fridge as it is the only condiment on the market that is FULL of REAL flavour.
Key Concepts:
FUNNY, URBAN, RELEVANT
FUNNY – Chaotic Adult fun. A strong sense of the child within.
NOT CHILDLIKE
URBAN – Stay away from the conservative “country image” that most of our competitors use. We don’t want to look like we were made out on a farm somewhere.
RELEVANT – THIS IS SOMETHING EVERYONE WILL WANT TO EAT!
It is relevant to everyone and will make everything they eat it with better. Everything.
Target Audience:
Our target audience is ANYONE who loves premium quality food and is willing to pay a little bit more for a great tasting product as opposed to settling for a cheaper relish that is below average, processed and filled with additives and nasties. Our current demographic is middle-class, comfortable income, mainly Anglo-Saxon Australians - age range is quite broad from young up to professionals to comfortably set retirees.
Non Negotiable Elements of the design: The Logo
Size: Postcard - PORTRAIT ORIENTATION
File format: Happy for you to suggest which format is best.
Stock : 350gsm paper
Colours: Dominant colour must be a “Roma Tomato” Red, however keep colours down to Maximum 4
Design:
Double sided .
Front will have writing as follows with long logo incorporated as well:
BRAMWELL & JORY (LOGO)
Relish just got saucy (this should fit right under the logo )
• 100% Natural
• Luscious Full Flavour
• Award Winning
• Gluten Free
• Vegan Friendly
• Modern Australian Taste
.........with echoes of tradition.
Makes everything better. Everything!
Back will have burger image with short logo above it
Updates
SORRY! Forgot to mention that design layout needs to be PORTRAIT. Thanks

```html
<!DOCTYPE html>
<html lang="en">
<head>
<meta charset="utf-8">
<title>Bramwell &amp; Jory Velvet Foods – Shelf Talker</title>
<link rel="stylesheet" href="https://fonts.googleapis.com/css2?family=Open+Sans:wght@400;600;700&family=PT+Serif:wght@700&family=Patrick+Hand&display=swap">
<style>
  :root {
    --roma-red: #a51c1c;
    --band-red: #a8190f;
    --ink: #333333;
    --frame: #555555;
    --card-edge: #8a8a8a;
    --paper: #ffffff;
    --tomato-light: #f4cdc5;
    --tomato-mid: #e8a79c;
    --parchment-light: #e8d8bb;
    --parchment-dark: #c4a57a;
  }
  * { box-sizing: border-box; margin: 0; padding: 0; }
  html, body { width: 1200px; height: 1001px; overflow: hidden; background: var(--paper); }
  .board {
    position: relative; width: 1200px; height: 1001px;
    border: 1px solid var(--frame); background: var(--paper);
    font-family: "Open Sans", Arial, sans-serif;
  }
  .corner-bar { position: absolute; background: var(--band-red); }
  .corner-bar--top { left: 2px; top: 2px; width: 164px; height: 29px; }
  .corner-bar--bottom { right: 0; bottom: 0; width: 163px; height: 29px; }

  /* Front card */
  .card-front {
    position: absolute; left: 67px; top: 203px; width: 475px; height: 616px;
    border: 1px solid var(--card-edge); overflow: hidden;
  }
  .front-photo {
    position: absolute; inset: 0;
    background: radial-gradient(circle at 30% 40%, var(--tomato-mid), var(--tomato-light) 70%);
  }
  .scroll {
    position: absolute; left: 34px; top: 4px; width: 404px; height: 214px;
    background: linear-gradient(135deg, var(--parchment-light), var(--parchment-dark));
    transform: rotate(-3deg);
  }
  .brand-lockup { position: absolute; left: 95px; top: 70px; width: 300px; text-align: center; transform: rotate(-3deg); }
  .brand-name { font-weight: 600; font-size: 40px; color: var(--roma-red); line-height: 1; letter-spacing: -0.5px; }
  .tagline { font-family: "Patrick Hand", cursive; font-size: 22px; color: var(--ink); margin-top: 4px; margin-left: 60px; text-align: left; }
  .benefits { position: absolute; left: 52px; top: 228px; list-style: none; }
  .benefits li {
    display: flex; align-items: flex-start; gap: 27px;
    font-weight: 600; font-size: 24px; color: var(--roma-red);
    line-height: 36px; margin-bottom: 16.5px;
  }
  .benefits svg { flex: none; width: 40px; height: 40px; margin-top: -2px; }
  .strapline {
    position: absolute; left: 0; right: 0; bottom: 0; height: 38px;
    background: var(--band-red); border-top: 3px solid #ffffff;
    font-family: "PT Serif", Georgia, serif; font-weight: 700; font-size: 20px;
    color: #ffffff; text-align: center; line-height: 35px; letter-spacing: 0.3px;
  }

  /* Back card */
  .card-back {
    position: absolute; left: 584px; top: 203px; width: 462px; height: 598px;
    border: 1px solid var(--card-edge); background: var(--paper); overflow: hidden;
  }
  .back-photo {
    position: absolute; left: 0; top: 0; width: 100%; height: 528px;
    background: linear-gradient(180deg, #e2b970 0%, #b7463a 22%, #7a5a6e 38%, #e9a23a 52%, #5a3a2a 66%, #7fae3e 82%, #e3cf9a 100%);
  }
  .back-logo-long { position: absolute; left: 37px; top: 548px; font-weight: 600; font-size: 36px; color: var(--ink); letter-spacing: -0.5px; }
  .back-logo-short {
    position: absolute; right: 12px; top: 538px; font-weight: 600; font-size: 21px;
    line-height: 22px; color: var(--roma-red); text-align: right;
  }
</style>
</head>
<body>
<div class="board">
  <div class="corner-bar corner-bar--top"></div>
  <div class="corner-bar corner-bar--bottom"></div>

  <section class="card-front">
    <div class="front-photo" role="img" aria-label="Soft close-up photograph of ripe Roma tomatoes"></div>
    <div class="scroll" role="img" aria-label="Aged parchment scroll banner"></div>
    <div class="brand-lockup">
      <div class="brand-name">Bramwell &amp; Jory</div>
      <div class="tagline">relish just got saucy</div>
    </div>
    <ul class="benefits">
      <li><svg viewBox="0 0 40 40" aria-hidden="true"><circle cx="20" cy="20" r="18" fill="#3a3a3a"/><path d="M4 24 A17 17 0 0 0 36 24 L30 22 A11 11 0 0 1 10 22 Z" fill="#a51c1c"/><path d="M11 20 L18 27 L30 12" fill="none" stroke="#fff" stroke-width="5" stroke-linecap="round" stroke-linejoin="round"/></svg>100% Natural</li>
      <li><svg viewBox="0 0 40 40" aria-hidden="true"><circle cx="20" cy="20" r="18" fill="#3a3a3a"/><path d="M4 24 A17 17 0 0 0 36 24 L30 22 A11 11 0 0 1 10 22 Z" fill="#a51c1c"/><path d="M11 20 L18 27 L30 12" fill="none" stroke="#fff" stroke-width="5" stroke-linecap="round" stroke-linejoin="round"/></svg>Luscious Full Flavour</li>
      <li><svg viewBox="0 0 40 40" aria-hidden="true"><circle cx="20" cy="20" r="18" fill="#3a3a3a"/><path d="M4 24 A17 17 0 0 0 36 24 L30 22 A11 11 0 0 1 10 22 Z" fill="#a51c1c"/><path d="M11 20 L18 27 L30 12" fill="none" stroke="#fff" stroke-width="5" stroke-linecap="round" stroke-linejoin="round"/></svg>Award Winning</li>
      <li><svg viewBox="0 0 40 40" aria-hidden="true"><circle cx="20" cy="20" r="18" fill="#3a3a3a"/><path d="M4 24 A17 17 0 0 0 36 24 L30 22 A11 11 0 0 1 10 22 Z" fill="#a51c1c"/><path d="M11 20 L18 27 L30 12" fill="none" stroke="#fff" stroke-width="5" stroke-linecap="round" stroke-linejoin="round"/></svg>Gluten Free</li>
      <li><svg viewBox="0 0 40 40" aria-hidden="true"><circle cx="20" cy="20" r="18" fill="#3a3a3a"/><path d="M4 24 A17 17 0 0 0 36 24 L30 22 A11 11 0 0 1 10 22 Z" fill="#a51c1c"/><path d="M11 20 L18 27 L30 12" fill="none" stroke="#fff" stroke-width="5" stroke-linecap="round" stroke-linejoin="round"/></svg>Vegan Friendly</li>
      <li><svg viewBox="0 0 40 40" aria-hidden="true"><circle cx="20" cy="20" r="18" fill="#3a3a3a"/><path d="M4 24 A17 17 0 0 0 36 24 L30 22 A11 11 0 0 1 10 22 Z" fill="#a51c1c"/><path d="M11 20 L18 27 L30 12" fill="none" stroke="#fff" stroke-width="5" stroke-linecap="round" stroke-linejoin="round"/></svg><span>Modern Australian Taste<br>with echoes of tradition</span></li>
    </ul>
    <div class="strapline">Makes everything better. Everything!</div>
  </section>

  <section class="card-back">
    <div class="back-photo" role="img" aria-label="Close-up photograph of a gourmet burger with relish, pickles, red onion, cheese and lettuce"></div>
    <div class="back-logo-long">Bramwell &amp; Jory</div>
    <div class="back-logo-short">Bramwell<br>&amp; Jory</div>
  </section>
</div>
</body>
</html>
```